Zielgruppe
Wir sind ein Restaurant und starten jetzt mit der Herstellung von eigenen Getränken wie z.B. Whisky, Gin, Rum, Weine, Liköre etc. Die erste Linie des Whiksy haben wir selbst entworfen möchten aber mehr Professionalität einbringen.
Aufgabenstellung
Beiliegend die beiden Flaschen welche bedruckt/beklebt werden (mit Flaschenbezeichnung) und unser LOGO als PSD.
Stichworte: Regional, Qualität, Beste Zutaten, keine Zusatzstoffe
Bezeichnungen: Silberfalter Whisky / Silberfalter Gin
Wichtig: Wiederkennungswert schaffen (Es sollen in Zukunft auch Weine, Liköre etc. produziert werden)
Infos Gin:
- 65 verschiedenen Botanicals
- Neben Blutorangen, Zitronen und Limetten, zeigt auch der Duft von Ingwer, Zitronengras und Kaffirlimettenblätter als Zitrusensemble das Facettenreichtum des Gins. Das Aromaspiel verändert sich nach etwas Zeit im Glas sehr deutlich. Dann zeigen sich starke Aromakomponenten wie Kardamom, Koriander oder Piment. Der Gin zeichnet sich aus durch seine Lebendigkeit
- 42%vol
- 500ml
Infos Whisky:
- 8 Jahre gereift
- Zur Vergärung unseres Whiskys verwenden wir eigens gezüchtete Frischhefe mit besonderen Fähigkeiten zur Bildung von sehr fruchtigen Gäraromen. Die Weichheit bekommt er durch die dreifache Destillation. Auch bei der Wahl unserer Gerste setzen wir auf unsere Region. Der Grund für diesen starken regionalen Bezug ist, dass wir versuchen unserem Whisky die größtmögliche Portion an Terroir zu verleihen. Bei der anschließenden Fasslagerung setzen wir auf hochwertige Fässer. Zuerst neue amerikanische Weißeiche mit anschließendem Sherry- und Cognacfass finish.
Tradition und Moderne verschmelzen zu einem unverwechselbaren Whisky, mit weichem, fruchtigen femininen Geschmack und wildem, maskulinen Charakter.
- Single Malt Whisky
- Geruch & Geschmack: Der Whisky zeichnet sich aus durch intensive, weiche Aromen nach Vanille und süßen Früchten, mit einem ungewöhnlich weichen und sanften Abgang mit einem Hauch von dunkler Schokolade.
Folgende obligatorischen Angaben sind Pflicht:
- Adresse 'Silberfalter / Lindenwiese 7 / 48213 Auenried-Talheim'
- Losnummer z.B. L0121..

```html
<!DOCTYPE html>
<html lang="de">
<head>
<meta charset="utf-8">
<title>Silberfalter Gin – Etikett</title>
<link rel="stylesheet" href="https://fonts.googleapis.com/css2?family=Archivo+Black&family=Arimo:ital,wght@0,400;0,700;1,700&family=Mrs+Saint+Delafield&display=swap">
<style>
  :root {
    --backdrop: #2b2b2d;
    --ink: #121212;
    --gold: #d9b13a;
    --gold-light: #f3d66e;
    --gold-deep: #9c7418;
    --white: #f4f4f4;
  }
  html, body {
    margin: 0;
    width: 1200px;
    height: 1200px;
    overflow: hidden;
    background: var(--backdrop);
  }
  .canvas {
    position: relative;
    width: 1200px;
    height: 1200px;
    background: radial-gradient(circle at 50% 45%, #3a3a3c 0%, var(--backdrop) 70%);
  }
  .label {
    position: absolute;
    left: 300px;
    top: 120px;
    width: 560px;
    height: 900px;
  }
  .label-shape {
    position: absolute;
    inset: 0;
  }
  .brand-seal {
    position: absolute;
    left: 180px;
    top: 30px;
    width: 156px;
    height: 156px;
    border: 2px solid var(--gold);
    border-radius: 50%;
    display: flex;
    align-items: center;
    justify-content: center;
    z-index: 3;
  }
  .brand-seal span {
    font-family: "Arimo", sans-serif;
    font-weight: 700;
    font-size: 20px;
    color: var(--gold-light);
    letter-spacing: 0.5px;
  }
  .brand-name {
    position: absolute;
    left: 12px;
    top: 160px;
    font-family: "Arimo", sans-serif;
    font-weight: 700;
    font-size: 24px;
    color: var(--gold);
    z-index: 3;
  }
  .product-word {
    position: absolute;
    left: 70px;
    top: 125px;
    font-family: "Archivo Black", sans-serif;
    font-size: 262px;
    line-height: 1;
    letter-spacing: -10px;
    color: var(--ink);
    z-index: 1;
  }
  .botanical {
    position: absolute;
    z-index: 2;
    background: radial-gradient(circle at 40% 40%, var(--gold-light), var(--gold) 55%, var(--gold-deep));
    opacity: 0.85;
  }
  .botanical.orange-slice { left: 60px; top: 320px; width: 105px; height: 120px; border-radius: 50%; }
  .botanical.leaf-left { left: 10px; top: 370px; width: 55px; height: 42px; border-radius: 50%; }
  .botanical.leaves { left: 235px; top: 255px; width: 105px; height: 105px; border-radius: 45% 55% 50% 50%; }
  .botanical.lemongrass { left: 345px; top: 270px; width: 20px; height: 90px; border-radius: 10px; }
  .botanical.coriander { left: 415px; top: 295px; width: 52px; height: 62px; border-radius: 50%; }
  .botanical.ginger { left: 475px; top: 340px; width: 62px; height: 48px; border-radius: 40% 60% 50% 45%; }
  .claims {
    position: absolute;
    left: 170px;
    top: 398px;
    width: 290px;
    text-align: center;
    font-family: "Arimo", sans-serif;
    font-weight: 700;
    font-style: italic;
    font-size: 14.5px;
    line-height: 22px;
    letter-spacing: 1.3px;
    color: var(--ink);
    z-index: 2;
  }
  .claims p { margin: 0; }
  .claims .aroma {
    font-family: "Mrs Saint Delafield", cursive;
    font-style: normal;
    font-weight: 400;
    font-size: 36px;
    line-height: 44px;
    letter-spacing: 0;
    margin: 2px -40px 2px 0;
  }
  .address {
    position: absolute;
    left: 30px;
    top: 815px;
    font-family: "Arimo", sans-serif;
    font-size: 9.5px;
    line-height: 13px;
    color: var(--white);
    transform: rotate(8deg);
    transform-origin: left top;
  }
  .address p { margin: 0; }
  .specs {
    position: absolute;
    right: 45px;
    top: 835px;
    display: flex;
    align-items: flex-start;
    font-family: "Arimo", sans-serif;
    color: var(--white);
  }
  .specs .details {
    font-size: 10px;
    line-height: 14px;
    padding: 6px 10px 0 0;
  }
  .specs .details p { margin: 0; }
  .specs .volume {
    border-left: 1.5px solid var(--white);
    height: 50px;
    padding-left: 5px;
    font-size: 13px;
  }
</style>
</head>
<body>
<main class="canvas">
  <section class="label">
    <svg class="label-shape" viewBox="0 0 560 900" width="560" height="900" aria-hidden="true">
      <defs>
        <linearGradient id="labelTone" x1="0" y1="0" x2="0" y2="1">
          <stop offset="0" stop-color="#5a5a5c"/>
          <stop offset="1" stop-color="#4e4e50"/>
        </linearGradient>
      </defs>
      <path d="M0 135 H168.35 A95 95 0 1 1 351.65 135 H560 V870 Q280 905 0 870 Z" fill="url(#labelTone)"/>
    </svg>

    <div class="brand-seal"><span>Silberfalter</span></div>
    <div class="brand-name">Silberfalter</div>
    <div class="product-word">GIN</div>

    <div class="botanical orange-slice" role="img" aria-label="Goldene Zeichnung einer Orangenscheibe"></div>
    <div class="botanical leaf-left" role="img" aria-label="Goldene Zeichnung eines Blattes"></div>
    <div class="botanical leaves" role="img" aria-label="Goldene Zeichnung von Kaffirlimettenblättern"></div>
    <div class="botanical lemongrass" role="img" aria-label="Goldene Zeichnung von Zitronengras"></div>
    <div class="botanical coriander" role="img" aria-label="Goldene Zeichnung von Koriander"></div>
    <div class="botanical ginger" role="img" aria-label="Goldene Zeichnung einer Ingwerwurzel"></div>

    <div class="claims">
      <p>100 % Natürliche Zutaten</p>
      <p>Mit Liebe handgemacht</p>
      <p>65 Botanicals</p>
      <p class="aroma">lebendiges Aroma</p>
      <p>Keine Zusatzstoffe</p>
      <p>Verdammt gute Qualität</p>
    </div>

    <div class="address">
      <p>Zum Silberfalter</p>
      <p>Lindenwiese 7 / 48213 Auenried-Talheim</p>
    </div>

    <div class="specs">
      <div class="details">
        <p>42% vol.</p>
        <p>L0121</p>
      </div>
      <div class="volume">500ml</div>
    </div>
  </section>
</main>
</body>
</html>
```